Kestrelwood Pathways Agency business cards

Australian company about to start offering its services. We recruit international students to come to study English, vocational education and postgraduate courses in Australia. We help them find the institution and select the right city they want to come to Australia. We are a young, online oriented and supportive agency. Our clients are between 18 and 35 years old, mainly University students, young professionals or people with work experience. We provide much more information that any other agency offer. We administrate a Facebook group with more than 11.000 members that daily ask questions about general information when coming to Australia, while they are here and even after they leave the country

Target Market(s)

International students from South America, Central America and Europe

Industry/Entity Type

Student

Contact Information for Business Card

Tomas Brevik
Managing Director
tomas@velmorin.com.au
www.velmorin.com.au
+61 491058263
Melbourne, Australia

Font styles to use
Serif
Sans Serif

Colors

Designer to choose colors to be used in the design.

Requirements
Must have
• Horizontal design
• Standard business card size and shape. If font uses green or yellow colours, they will have to match the ones from the logo
Nice to have
• UPDATE: Use the contents of the green image to design one of the card sides. Use our logo in the background of that side as watermark.
• Passport image, or immigration stamps. A picture of the Yarra River (from Melbourne) would be cool as well.
Should not have
• Non-standard business card size and shape
• Not black as the background colour of any sides as we are not a VIP agency or a hight class service. We are orientes to young people and they like colours, pictures, something attractive.
• Vertical design
• NO YELLOW or BLACK AS THE BACKGROUND COLOUR OF ANY SIDE OF THE BIZ CARD

```html
<!DOCTYPE html>
<html lang="en">
<head>
<meta charset="utf-8">
<title>Kestrelwood Pathways Agency – Business Card</title>
<link href="https://fonts.googleapis.com/css2?family=Delius&family=Open+Sans:wght@400&display=swap" rel="stylesheet">
<style>
  :root {
    --page-bg: #dcd8d1;
    --card-dark: #0c3326;
    --card-mid: #17473a;
    --card-light: #235a4a;
    --accent-orange: #e39a1f;
    --text-light: #e9ece8;
    --text-soft: #c9d1cc;
  }
  html, body {
    margin: 0;
    padding: 0;
    width: 1200px;
    height: 969px;
    overflow: hidden;
    background: var(--page-bg);
  }
  .business-card {
    position: absolute;
    left: 100px;
    top: 200px;
    width: 1000px;
    height: 568px;
    border-radius: 22px;
    background:
      radial-gradient(ellipse 60% 70% at 62% 45%, var(--card-light) 0%, transparent 70%),
      linear-gradient(135deg, var(--card-mid) 0%, var(--card-dark) 100%);
    box-shadow: 0 10px 30px rgba(0,0,0,0.25);
    overflow: hidden;
  }
  .brand-name {
    position: absolute;
    left: 45px;
    top: 92px;
    margin: 0;
    font-family: "Delius", cursive;
    font-weight: 400;
    font-size: 56px;
    line-height: 1;
    color: var(--accent-orange);
  }
  .contact-block {
    position: absolute;
    left: 45px;
    top: 258px;
  }
  .person-name {
    margin: 0;
    font-family: "Delius", cursive;
    font-size: 33px;
    line-height: 1.2;
    color: var(--accent-orange);
  }
  .person-role {
    margin: 2px 0 0;
    font-family: "Delius", cursive;
    font-size: 24px;
    line-height: 1.2;
    color: var(--text-light);
  }
  .person-location {
    margin: 16px 0 14px;
    font-family: "Open Sans", sans-serif;
    font-size: 21px;
    color: var(--text-soft);
  }
  .contact-list {
    list-style: none;
    margin: 0;
    padding: 0;
  }
  .contact-item {
    display: flex;
    align-items: center;
    gap: 14px;
    height: 32px;
    font-family: "Open Sans", sans-serif;
    font-size: 21px;
    color: var(--text-soft);
  }
  .contact-icon {
    width: 20px;
    height: 20px;
    flex: none;
    margin-left: 10px;
  }
  .tagline {
    margin: 22px 0 0;
    font-family: "Delius", cursive;
    font-size: 24px;
    color: var(--accent-orange);
  }
</style>
</head>
<body>
  <div class="business-card">
    <p class="brand-name">Velmorin</p>

    <div class="contact-block">
      <p class="person-name">Tomas Brevik</p>
      <p class="person-role">Managing Director</p>
      <p class="person-location">Melbourne, Australia</p>
      <ul class="contact-list">
        <li class="contact-item">
          <svg class="contact-icon" viewBox="0 0 20 20" aria-hidden="true">
            <path fill="#e39a1f" d="M4.5 1.5l3 3.2-1.6 2.3c1 2.2 2.8 4 5 5l2.3-1.6 3.3 3-1.5 3.2C8.6 16.4 3.6 11.4 1.3 3z"/>
          </svg>
          <span>+61 491058263</span>
        </li>
        <li class="contact-item">
          <svg class="contact-icon" viewBox="0 0 20 20" aria-hidden="true">
            <rect x="1.5" y="4" width="17" height="12" rx="1.5" fill="#e39a1f"/>
            <path d="M2 5l8 6 8-6" fill="none" stroke="#0c3326" stroke-width="1.5"/>
          </svg>
          <span>tomas@velmorin.com.au</span>
        </li>
        <li class="contact-item">
          <svg class="contact-icon" viewBox="0 0 20 20" aria-hidden="true">
            <circle cx="10" cy="10" r="8.5" fill="#e39a1f"/>
            <path d="M1.5 10h17M10 1.5c-3 3-3 14 0 17M10 1.5c3 3 3 14 0 17" fill="none" stroke="#0c3326" stroke-width="1.3"/>
          </svg>
          <span>www.velmorin.com.au</span>
        </li>
      </ul>
      <p class="tagline">Hacemos más por ti!</p>
    </div>
  </div>
</body>
</html>
```